Attorney Website Design

I need a top quality attorney website layout designed. Here are some examples of what I feel are great websites:
http://www.quellmarstonseparationlaw.com/
http://www.vandriclegalgroup.com/
http://www.pobelaw.com/
http://www.harrowvaleaccusedcounselhq.com/
http://www.tzlegal.com/
http://www.brookhollowtrialjusticeoffice.com/
http://www.orvynchargedcounsel.com/
http://www.tzlegal.com/
What we like about these sites:
• The different layers
• Subtle designs, textures, curves
• 3 dimensional
• Floating effects
• Prominent phone number
• Location of Areas of Practice
• Request A Consultation Prominent
• Right side bar with practice areas
• Badges
• Clear Calls to Action
• Dynamic/Staying Top navigation when you scroll
The project will be for a home page and then also an interior page (should be similar to home page).
Updates
I want to make it understood I am looking for a design which is not a typical "template" site which I can find anywhere for $50. This budget and project is for a "Custom" website design. Please submit designs similar in quality to the samples links I have posted. Creativity is a MUST! The best way to explain this is, I want a design that I can feel it unique and original, not something that looks like 95% of all websites out there.
Neil
I just wanted everyone to know that so far I am not to pleased with any of the designs. I am not looking for cut/pasting of other peoples websites but ORIGINAL and CREATIVE work.
Reason: Weekend + Holiday extension.
Reason: Need more designs
Industry/Entity Type
Attorney

```html
<!DOCTYPE html>
<html lang="en">
<head>
<meta charset="utf-8">
<title>Brackwell Attorneys</title>
<link rel="stylesheet" href="https://fonts.googleapis.com/css2?family=Open+Sans:wght@400;600&family=Tinos&display=swap">
<style>
:root{
  --red:#b3302b;
  --red-dark:#9b1c1c;
  --ink:#2b2b2b;
  --text:#555;
  --muted:#999;
  --line:#e4e4e4;
  --panel:#f3f2f1;
  --footer:#3a3a3a;
}
*{margin:0;padding:0;box-sizing:border-box}
html,body{width:1200px;height:1133px;overflow:hidden;background:#fff}
body{position:relative;font-family:"Open Sans",Arial,sans-serif;color:var(--text)}
a{color:inherit;text-decoration:none}

.site-header{position:absolute;left:0;top:0;width:1200px;height:91px;background:#fff;border-bottom:3px solid var(--red)}
.brand{position:absolute;left:110px;top:30px;font-size:21px;font-weight:600;color:var(--red);letter-spacing:.3px;line-height:1}
.main-nav{position:absolute;left:520px;top:30px;display:flex}
.main-nav a{display:block;height:31px;line-height:31px;padding:0 11px;font-size:13px;color:var(--ink);text-transform:uppercase;white-space:nowrap}
.main-nav a.active{background:var(--red);color:#fff;padding:0 16px;margin-right:10px}
.main-nav a:last-child{padding-right:0}

.hero-band{position:absolute;left:0;top:91px;width:1200px;height:547px;background:radial-gradient(ellipse at 50% 10%,#444 0%,#333 55%,#2b2b2b 100%)}
.hero-title{position:absolute;left:0;top:112px;width:1200px;text-align:center;font-family:"Tinos",Georgia,serif;font-size:26px;color:#fff;font-weight:400}
.hero-lead{position:absolute;left:150px;top:148px;width:900px;text-align:center;font-size:14px;line-height:20px;color:#ddd}
.fade-band{position:absolute;left:0;top:638px;width:1200px;height:90px;background:linear-gradient(#e6e6e6,#fff)}

.slider{position:absolute;left:110px;top:216px;width:980px;height:465px;border-bottom:3px solid var(--red)}
.slide-photo{position:absolute;inset:0;background:linear-gradient(115deg,#2a2422 0%,#3b302b 30%,#8a7562 55%,#d9cbb7 78%,#efe7dc 100%)}
.slider-dots{position:absolute;left:19px;top:433px;display:flex;gap:3px}
.slider-dots span{width:10px;height:10px;border-radius:50%;background:rgba(255,255,255,.45)}
.slider-dots span.on{background:#fff}

.finder{position:absolute;left:716px;top:63px;width:243px;height:293px;background:rgba(248,246,244,.9);border-radius:4px;box-shadow:0 0 4px rgba(0,0,0,.15);padding:0 12px}
.finder h2{font-size:20px;font-weight:400;color:var(--ink);height:52px;line-height:52px;border-bottom:1px solid var(--line)}
.finder label{display:block;font-size:12px;color:var(--ink);margin-top:5px;height:22px;line-height:22px}
.finder .field{height:32px;background:#fff;border:1px solid #e2e2e2;border-radius:3px;font-size:10px;font-style:italic;color:#aaa;line-height:30px;padding-left:9px}
.finder .btn{display:inline-block;margin-top:14px;background:var(--red);color:#fff;font-size:13px;height:32px;line-height:32px;padding:0 9px;margin-left:1px}

.col-title{position:absolute;top:716px;font-size:20px;font-weight:400;color:var(--ink)}
.services-intro{position:absolute;left:110px;top:750px;width:240px;font-size:12.5px;line-height:20px;color:var(--text);padding-bottom:11px;border-bottom:1px solid var(--line)}
.service-list{position:absolute;left:110px;top:831px;list-style:none}
.service-list li{height:25px;display:flex;align-items:center;font-size:13px;color:var(--muted)}
.service-list li a{text-decoration:underline}
.service-list svg{margin-right:9px}

.article{position:absolute;left:378px;top:755px;width:441px;height:292px;background:var(--panel);border-radius:0 4px 4px 0}
.article-photo{position:absolute;left:0;top:0;width:226px;height:292px;background:linear-gradient(160deg,#dfe4ea 0%,#b8c2cc 45%,#6f6558 75%,#c9b48a 100%);border-right:5px solid #e3e1de}
.article-body{position:absolute;left:247px;top:20px;width:180px}
.article-date{font-size:12px;color:#666}
.article-title{margin-top:10px;font-size:15px;line-height:20px;color:var(--red);font-weight:400;text-transform:uppercase}
.article-text{margin-top:8px;font-size:12.5px;line-height:20px;color:#777}
.article .btn{display:inline-block;margin-top:16px;background:var(--red);color:#fff;font-size:14px;height:32px;line-height:32px;padding:0 9px}

.lawyer{position:absolute;left:849px;display:flex}
.lawyer-photo{width:77px;height:73px;border:2px solid #fff;box-shadow:0 0 3px rgba(0,0,0,.3);background:linear-gradient(135deg,#b9b3a9,#6d645a 60%,#2f2a27)}
.lawyer-info{margin-left:15px;padding-top:13px}
.lawyer-name{font-size:16px;color:var(--red-dark);text-transform:uppercase}
.lawyer-place{font-size:14px;color:#777;margin-top:2px}
.view-all{position:absolute;left:1040px;top:1027px;font-size:14px;color:var(--red);text-decoration:underline}

.site-footer{position:absolute;left:0;top:1081px;width:1200px;height:52px;background:var(--footer);color:#ddd;font-size:13px;text-align:center;line-height:54px}
</style>
</head>
<body>
<header class="site-header">
  <div class="brand">BRACKWELL ATTORNEYS</div>
  <nav class="main-nav">
    <a class="active" href="#">Home</a>
    <a href="#">Know Your Rights</a>
    <a href="#">Check the News</a>
    <a href="#">Read Articles</a>
    <a href="#">Contact Us</a>
  </nav>
</header>

<section class="hero-band"></section>
<div class="fade-band"></div>
<h1 class="hero-title">Common Law Adjudication</h1>
<p class="hero-lead">Lorem ipsum dolor sit amet, consectetur adipisicing elit, sed do eiusmod tempor incididunt ut labore et dolore magna aliqua. Ut enim ad minim veniam, quis nostrud exercitation ullamco laboris nisi ut aliquip ex ea commodo consequat.</p>

<div class="slider">
  <div class="slide-photo" role="img" aria-label="Lawyer in a suit leafing through a thick law book at a desk with papers and a pen"></div>
  <div class="slider-dots"><span></span><span class="on"></span><span></span><span></span><span></span></div>
  <form class="finder">
    <h2>Find a Lawyers</h2>
    <label>Lawyer's Name :</label>
    <div class="field">enter here...</div>
    <label>Law Firm Name :</label>
    <div class="field">enter here...</div>
    <label>Location :</label>
    <div class="field">enter here...</div>
    <a class="btn" href="#">FIND A LAWYER</a>
  </form>
</div>

<h2 class="col-title" style="left:110px">Our Services</h2>
<p class="services-intro">Lorem ipsum dolor sit amet, consectetur adipisicing elit, sed do eiusmod tempor incididunt magna aliqua.</p>
<ul class="service-list">
  <li><svg width="14" height="14" viewBox="0 0 14 14"><circle cx="7" cy="7" r="7" fill="#ddd"/><path d="M4 7h5M7 4.5L9.5 7 7 9.5" stroke="#fff" stroke-width="1.5" fill="none"/></svg><a href="#">Criminal Defense Attorney</a></li>
  <li><svg width="14" height="14" viewBox="0 0 14 14"><circle cx="7" cy="7" r="7" fill="#ddd"/><path d="M4 7h5M7 4.5L9.5 7 7 9.5" stroke="#fff" stroke-width="1.5" fill="none"/></svg><a href="#">Florida Divorce Lawyer</a></li>
  <li><svg width="14" height="14" viewBox="0 0 14 14"><circle cx="7" cy="7" r="7" fill="#ddd"/><path d="M4 7h5M7 4.5L9.5 7 7 9.5" stroke="#fff" stroke-width="1.5" fill="none"/></svg><a href="#">Divorce Law Attorneys</a></li>
  <li><svg width="14" height="14" viewBox="0 0 14 14"><circle cx="7" cy="7" r="7" fill="#ddd"/><path d="M4 7h5M7 4.5L9.5 7 7 9.5" stroke="#fff" stroke-width="1.5" fill="none"/></svg><a href="#">Miami Attorneys</a></li>
  <li><svg width="14" height="14" viewBox="0 0 14 14"><circle cx="7" cy="7" r="7" fill="#ddd"/><path d="M4 7h5M7 4.5L9.5 7 7 9.5" stroke="#fff" stroke-width="1.5" fill="none"/></svg><a href="#">Attorneys Orlando FL</a></li>
  <li><svg width="14" height="14" viewBox="0 0 14 14"><circle cx="7" cy="7" r="7" fill="#ddd"/><path d="M4 7h5M7 4.5L9.5 7 7 9.5" stroke="#fff" stroke-width="1.5" fill="none"/></svg><a href="#">Attorneys in Tampa</a></li>
  <li><svg width="14" height="14" viewBox="0 0 14 14"><circle cx="7" cy="7" r="7" fill="#ddd"/><path d="M4 7h5M7 4.5L9.5 7 7 9.5" stroke="#fff" stroke-width="1.5" fill="none"/></svg><a href="#">Divorce Attorneys Tampa FL</a></li>
  <li><svg width="14" height="14" viewBox="0 0 14 14"><circle cx="7" cy="7" r="7" fill="#ddd"/><path d="M4 7h5M7 4.5L9.5 7 7 9.5" stroke="#fff" stroke-width="1.5" fill="none"/></svg><a href="#">Florida Criminal Attorneys</a></li>
</ul>

<h2 class="col-title" style="left:377px">Our Articles</h2>
<article class="article">
  <div class="article-photo" role="img" aria-label="Two business people shaking hands across a meeting table"></div>
  <div class="article-body">
    <div class="article-date">February 21, 2014</div>
    <h3 class="article-title">Weekend Update: Lorem Ipsum Dolor Sit Amet</h3>
    <p class="article-text">Lorem ipsum dolor sit amet, consectetur adipisicing elit, sed do eiusmod tempor incididunt ut labore et dolore magna aliqua.</p>
    <a class="btn" href="#">READ MORE</a>
  </div>
</article>

<h2 class="col-title" style="left:849px">Our Lawyer’s</h2>
<div class="lawyer" style="top:753px">
  <div class="lawyer-photo" role="img" aria-label="Portrait of lawyer Tom Hadley"></div>
  <div class="lawyer-info"><div class="lawyer-name">Tom Hadley</div><div class="lawyer-place">USA</div></div>
</div>
<div class="lawyer" style="top:844px">
  <div class="lawyer-photo" role="img" aria-label="Portrait of lawyer Allan Mercer"></div>
  <div class="lawyer-info"><div class="lawyer-name">Allan Mercer</div><div class="lawyer-place">Germany</div></div>
</div>
<div class="lawyer" style="top:935px">
  <div class="lawyer-photo" role="img" aria-label="Portrait of lawyer Jessica Varnell"></div>
  <div class="lawyer-info"><div class="lawyer-name">Jessica Varnell</div><div class="lawyer-place">Ireland</div></div>
</div>
<a class="view-all" href="#">View All</a>

<footer class="site-footer">Copy rigthe 2014 © Brackwell Attorneys. All rights reserved</footer>
</body>
</html>
```